Zielgruppe
Ich biete Marketing und Beratung an. Meine Zielgruppe sind KMU's aber auch Einzelfirmen welche selbst keine Marketingabteilung haben.
Aufgabenstellung
Sie sollen mein bestehendes CI/CD von meiner Website www.velorusk.ch möglichst mit Farben, Formen und Schriften übernehmen. Es soll eine einfache Seite mit 3 Rubriken werden. Über mich / Mein Angebot (Philosophie, Schwerpunkte/Preise) / Kontakt. Impressum, AGB und Datenschutz sollen CH Konform integriert sein. Ich habe meine Domain bei serwanox.ch registriert. Diese soll dann für die neue Website eingerichtet werden und von der Pixolo Seite entfernt werden. Der Link für Kontrabu soll funktionieren. Bilder können von der Pixolo Seite entnommen werden. Da ich für meine Kunden viele Websiten erstellen lassen werde, suche ich einen Designer*in mit welcher ich auch nach dieser Website zusammen arbeiten könnte. Die Seite möchte ich danach selber pflegen können. Es wäre toll wenn sie mit Wordpress erstellt wird (muss aber nicht sein).

```html
<!DOCTYPE html>
<html lang="de">
<head>
<meta charset="utf-8">
<title>velorusk – Marketing &amp; Beratung</title>
<link rel="stylesheet" href="https://fonts.googleapis.com/css2?family=Hind:wght@500;600;700&family=Open+Sans:wght@400;600&family=Ms+Madi&display=swap">
<style>
:root{
  --green:#14a065;
  --mint:#bbf0d2;
  --mint-soft:#d6f5e4;
  --ink:#262626;
  --text:#333;
  --page:#f5f5f5;
  --white:#fff;
}
*{box-sizing:border-box;margin:0;padding:0}
html,body{width:1200px;height:2421px;overflow:hidden}
body{position:relative;background:var(--page);font-family:"Open Sans",sans-serif;color:var(--text)}
.abs{position:absolute}
.head{font-family:"Hind",sans-serif;font-weight:700}
.script{font-family:"Ms Madi",cursive;color:var(--green)}

.bg-white-band{left:0;top:990px;width:1200px;height:760px;background:var(--white)}
.curve{left:0;width:1200px}

.brand{left:150px;top:22px;font-family:"Hind",sans-serif;font-weight:700;font-size:40px;color:var(--ink);letter-spacing:-1px}
.nav{top:38px;left:457px;display:flex;gap:41px;font-family:"Hind",sans-serif;font-weight:700;font-size:13px;color:var(--ink)}
.nav .active{position:relative}
.nav .active::after{content:"";position:absolute;left:17px;right:17px;bottom:-10px;height:3px;background:var(--green);border-radius:2px}
.follow{left:888px;top:28px;font-size:22px}
.follow-name{left:1024px;top:38px;font-family:"Hind",sans-serif;font-weight:700;font-size:13px;color:var(--green);display:flex;align-items:center;gap:5px}
.follow-name i{width:10px;height:10px;background:var(--green);display:inline-block}

.hero{left:150px;top:87px;width:900px;height:469px;background:linear-gradient(90deg,#d3f2e1,#b9ecd0);overflow:hidden}
.hero-scene{left:0;top:0;width:900px;height:469px;background:linear-gradient(135deg,rgba(150,200,170,.25),rgba(120,180,150,.35))}
.portrait{left:893px;top:183px;width:216px;height:373px;background:linear-gradient(180deg,#cfcfcf,#8a8a8a);border-radius:100px 100px 0 0}
.headline{left:232px;top:262px;font-size:51px;line-height:50px;color:var(--green);text-transform:uppercase}
.headline span{color:var(--white)}
.btn{top:438px;height:37px;border-radius:19px;font-family:"Hind",sans-serif;font-weight:700;font-size:15px;display:flex;align-items:center;justify-content:center}
.btn-solid{left:231px;width:192px;background:var(--green);color:var(--white)}
.btn-line{left:448px;width:160px;border:2px solid var(--green);color:var(--green)}

.services{left:87px;top:556px;width:1026px;height:61px;background:var(--white);box-shadow:0 3px 8px rgba(0,0,0,.08);border-radius:3px;display:flex;align-items:center;justify-content:center;gap:22px;font-family:"Hind",sans-serif;font-weight:700;font-size:12.5px;color:var(--ink)}
.services li{list-style:none;display:flex;align-items:center;gap:2px}
.tick{width:9px;height:9px}

.section-title{width:1200px;left:0;text-align:center;font-size:31px;color:var(--ink)}
.qmark{left:592px;top:666px;font-size:60px;color:var(--mint);line-height:1}
.lead{left:250px;width:700px;text-align:center;font-size:13.4px;line-height:20px}

.word{top:902px;height:86px}
.word .dot{position:absolute;top:4px;width:81px;height:81px;border-radius:50%;background:var(--mint)}
.word .arc{position:absolute;top:-2px}
.word .big{position:absolute;top:28px;font-family:"Hind",sans-serif;font-weight:700;font-size:32px;color:var(--green);white-space:nowrap}
.word .small{position:absolute;top:42px;font-family:"Hind",sans-serif;font-weight:600;font-size:14px;color:#2fb377;white-space:nowrap}

.quote{left:150px;top:1145px;width:900px;height:149px;background:var(--mint);border-radius:3px;display:flex;align-items:center;justify-content:center;text-align:center;font-size:21px;line-height:30px;color:var(--green)}

.card{top:1598px;width:267px;height:272px;border-radius:3px;box-shadow:2px 3px 6px rgba(0,0,0,.12);overflow:hidden;padding:22px 22px}
.card h3{font-size:16px;color:var(--ink);margin-bottom:14px}
.card ul{list-style:none;font-size:10.5px;font-weight:600;line-height:14px}
.card li{margin-bottom:11px;display:flex;gap:2px}
.card-a{left:150px;background:var(--mint)}
.card-b{left:467px;background:linear-gradient(180deg,#c2eed5,#b3e6c9)}
.card-c{left:783px;background:var(--green);color:var(--white)}
.card-c h3{color:var(--white)}
.card-c p{font-size:10.5px;line-height:15px}
.price{position:absolute;right:12px;bottom:-30px;width:118px;height:118px;border-radius:50%;background:var(--white);display:flex;align-items:flex-start;justify-content:center;padding-top:34px;font-size:24px;color:var(--green)}
.card-cta{position:absolute;left:27px;top:203px;width:177px;height:36px;border:2px solid var(--white);border-radius:18px;display:flex;align-items:center;justify-content:center;font-family:"Hind",sans-serif;font-weight:700;font-size:12px}

.portrait-small{left:150px;top:2016px;width:160px;height:272px;background:linear-gradient(180deg,#d0d0d0,#8c8c8c);border-radius:80px 80px 0 0}
.closing{left:376px;top:2105px;font-size:42px;line-height:40px}

.contact{left:87px;top:2288px;width:1026px;height:61px;background:var(--white);box-shadow:0 3px 8px rgba(0,0,0,.08);display:flex;align-items:center}
.contact-name{width:337px;height:61px;background:var(--green);color:var(--white);font-family:"Hind",sans-serif;font-weight:600;font-size:17px;display:flex;align-items:center;padding-left:63px}
.contact-item{display:flex;align-items:center;gap:14px;font-size:13px;color:var(--ink)}
.legal{top:2381px;font-size:9.5px;color:var(--ink)}
</style>
</head>
<body>

<div class="abs bg-white-band"></div>
<svg class="abs curve" style="top:960px" width="1200" height="90" viewBox="0 0 1200 90" aria-hidden="true"><path d="M0 30 Q600 120 1200 30 L1200 0 L0 0Z" fill="var(--page)"/></svg>
<svg class="abs curve" style="top:1720px" width="1200" height="60" viewBox="0 0 1200 60" aria-hidden="true"><path d="M0 60 Q600 -30 1200 60Z" fill="var(--page)"/></svg>
<div class="abs" style="left:0;top:1760px;width:1200px;height:661px;background:var(--page)"></div>

<header>
  <div class="abs brand">velorusk</div>
  <nav class="abs nav"><span>ÜBER MICH</span><span class="active">MEIN ANGEBOT</span><span>KONTAKT</span></nav>
  <div class="abs follow script">Folgen Sie mir auf</div>
  <div class="abs follow-name"><i></i>Kontrabu</div>
</header>

<section class="abs hero">
  <div class="abs hero-scene" role="img" aria-label="Blasses Foto eines Arbeitsplatzes mit Laptop und Pflanzen in Grüntönen"></div>
</section>
<div class="abs portrait" role="img" aria-label="Schwarzweiss-Porträt der Beraterin mit verschränkten Armen"></div>
<h1 class="abs headline head">Klar<span>.</span><br>Inspirierend<span>.</span><br>Wirksam<span>.</span></h1>
<div class="abs btn btn-solid">KOSTENLOSE OFFERTE</div>
<div class="abs btn btn-line">MEHR ÜBER MICH</div>

<ul class="abs services">
  <li><svg class="tick" viewBox="0 0 10 10"><path d="M1 5l3 3 5-7" stroke="#8fe0b5" stroke-width="2" fill="none"/></svg>MARKETING-STRATEGIE</li>
  <li><svg class="tick" viewBox="0 0 10 10"><path d="M1 5l3 3 5-7" stroke="#8fe0b5" stroke-width="2" fill="none"/></svg>BRANDING</li>
  <li><svg class="tick" viewBox="0 0 10 10"><path d="M1 5l3 3 5-7" stroke="#8fe0b5" stroke-width="2" fill="none"/></svg>PRODUCT MANEGEMENT</li>
  <li><svg class="tick" viewBox="0 0 10 10"><path d="M1 5l3 3 5-7" stroke="#8fe0b5" stroke-width="2" fill="none"/></svg>WERBE- &amp; KOMMUNIKATIONSPLANUNG</li>
  <li><svg class="tick" viewBox="0 0 10 10"><path d="M1 5l3 3 5-7" stroke="#8fe0b5" stroke-width="2" fill="none"/></svg>BERATUNG</li>
  <li><svg class="tick" viewBox="0 0 10 10"><path d="M1 5l3 3 5-7" stroke="#8fe0b5" stroke-width="2" fill="none"/></svg>EVENTS. WORKSHOPS &amp; SCHULUNGEN</li>
</ul>

<div class="abs qmark head">?</div>
<h2 class="abs section-title head" style="top:706px">Was steht hinter velorusk</h2>
<p class="abs lead" style="top:766px">Lorem ipsum dolor sit amet, consetetur sadipscing elitr, sed diam nonumy eirmod tempor invidunt ut labore et dolore magna aliquyam erat, sed diam voluptua. At vero eos et accusam et justo duo dolores et ea rebum. Stet clita kasd gubergren, no sea takimata sanctus est Lorem ipsum dolor sit amet. Lorem ipsum dolor sit amet, consetetur sadipscing elitr, sed diam nonumy eirmod tempor invidunt ut.</p>

<div class="abs word" style="left:258px">
  <svg class="arc" style="left:20px" width="60" height="40"><path d="M5 38 A45 45 0 0 1 55 3" stroke="var(--mint)" stroke-width="2" fill="none"/></svg>
  <div class="dot" style="left:27px"></div><span class="big">Mark</span><span class="small" style="left:78px">branding</span>
</div>
<div class="abs word" style="left:468px">
  <svg class="arc" style="left:20px" width="60" height="40"><path d="M5 38 A45 45 0 0 1 55 3" stroke="var(--mint)" stroke-width="2" fill="none"/></svg>
  <div class="dot" style="left:27px"></div><span class="big">Markt</span><span class="small" style="left:91px">business</span>
</div>
<div class="abs word" style="left:688px">
  <svg class="arc" style="left:20px" width="60" height="40"><path d="M5 38 A45 45 0 0 1 55 3" stroke="var(--mint)" stroke-width="2" fill="none"/></svg>
  <div class="dot" style="left:29px"></div><span class="big">rusk</span><span class="small" style="left:72px">erzeugen, erneuern, kreieren</span>
</div>

<blockquote class="abs quote head">“Durch meine Marketing Expertise hole ich das Beste aus Ihrem<br>Unternehmen heraus.”</blockquote>

<h2 class="abs section-title head" style="top:1413px">Angebote</h2>
<p class="abs lead" style="top:1469px">Lorem ipsum dolor sit amet, consetetur sadipscing elitr, sed diam nonumy eirmod tempor invidunt ut labore et dolore magna aliquyam erat, sed diam voluptua. At vero eos et accusam et justo duo dolores et ea rebum. Stet clita kasd gubergren, no sea takimata sanctus est Lorem ipsum dolor sit amet. Lorem ipsum dolor sit amet, consetetur sadipscing elitr, sed diam nonumy eirmod tempor invidunt ut.</p>

<article class="abs card card-a">
  <h3 class="head">EINZELSTUNDEN</h3>
  <ul><li>· Erstellen der Marketing-Strategie</li><li>· Sortimentsanalysen mit Massnahmen</li><li>· Branding</li><li>· Social Media Inhalte</li><li>· Website</li></ul>
  <div class="price head">180 CHF</div>
</article>
<article class="abs card card-b">
  <h3 class="head">HALBTAGE</h3>
  <ul><li>· Coaching für ein spezifisches Projekt,<br>Mitarbeit im Unternehmen etc.</li><li>· Lancierung von Produkten</li><li>· Relaunch</li><li>· Marktanalysen</li></ul>
  <div class="price head">580 CHF</div>
</article>
<article class="abs card card-c">
  <h3 class="head">KOSTENLOSE OFFERTE</h3>
  <p>Jede Zusammenarbeit wird individuell offeriert und basiert auf einem gemeinsam abgemachten Projektrahmen.</p>
  <div class="card-cta">KONTAKT AUFNEHMEN</div>
</article>

<div class="abs portrait-small" role="img" aria-label="Schwarzweiss-Porträt der Beraterin"></div>
<p class="abs closing script">Ich freue mich auf Sie<br>und ihr Projekt!</p>

<footer>
  <div class="abs contact">
    <div class="contact-name">Velorusk Mirelka Dorn GmbH</div>
    <div class="contact-item" style="margin-left:32px"><svg width="16" height="18" viewBox="0 0 16 18"><path d="M8 17s6-6 6-10A6 6 0 0 0 2 7c0 4 6 10 6 10z" stroke="var(--green)" fill="none"/><circle cx="8" cy="7" r="2" stroke="var(--green)" fill="none"/></svg>Lindenweg 4 CH-6300 Talheim</div>
    <div class="contact-item" style="margin-left:36px"><svg width="18" height="18" viewBox="0 0 18 18"><path d="M4 1l3 4-2 2a10 10 0 0 0 6 6l2-2 4 3-2 3C8 17 1 10 1 3z" stroke="var(--green)" fill="none"/></svg>+41 79 000 12 34</div>
    <div class="contact-item" style="margin-left:36px"><svg width="18" height="14" viewBox="0 0 18 14"><rect x="1" y="1" width="16" height="12" stroke="var(--green)" fill="none"/><path d="M1 1l8 7 8-7" stroke="var(--green)" fill="none"/></svg>info@velorusk.ch</div>
  </div>
  <div class="abs legal" style="left:150px">© Mirelka Dorn 2026</div>
  <div class="abs legal" style="right:150px">Impressum | Datenschutzerklärung | AGB</div>
</footer>

</body>
</html>
```